HVL Regal Business Card Design 2020

Harbor Vale Living is looking for a business card that is clean and straight to the point but still looks high-end and attractive. We are a team comprised of management and field professionals focused on the high-end residential marketplace. We serve homeowners and trade professionals directly based out of the Metrowest/Boston area. We provide client services as well as construction/renovation services.
We are aiming for a black and white feel (white background and black text) and a matte finish with rounded edges.

We want to emphasis our vision of "Properties - Projects - Partners".
Dana Pritchell is the president of HVL

Please include the following areas we service: Boston/Cape/Newport
Please make sure to include Dana's mobile (617) 555 0143 & office number (617) 555 0187, email dana@harborvaleliving.example and website www.harborvaleliving.example

Colors

Designer to choose only greyscale colors for use in the design.

Requirements
Must have
• Include "Properties - Projects - Partners" in design

Include "After Hours Emergency Support # 1800 555 0199" with icon

```html
<!DOCTYPE html>
<html lang="en">
<head>
<meta charset="utf-8">
<title>Harbor Vale Living – Business Card</title>
<link href="https://fonts.googleapis.com/css2?family=Montserrat:wght@700;800&family=Source+Sans+3:wght@400;600&display=swap" rel="stylesheet">
<style>
  :root {
    --backdrop: #e2e2e2;
    --backdrop-light: #efefef;
    --card-dark: #323232;
    --card-light: #f4f4f4;
    --ink: #2f2f2f;
    --ink-soft: #3a3a3a;
    --paper: #ffffff;
    --shadow: rgba(0, 0, 0, 0.35);
  }
  * { margin: 0; padding: 0; box-sizing: border-box; }
  html, body { width: 1200px; height: 960px; overflow: hidden; }
  body {
    position: relative;
    background: radial-gradient(ellipse at center, var(--backdrop-light) 0%, var(--backdrop) 75%);
    font-family: "Source Sans 3", "Myriad Pro", sans-serif;
    color: var(--ink);
  }
  .card {
    position: absolute;
    left: 310px;
    width: 581px;
    height: 333px;
    box-shadow: 3px 4px 6px var(--shadow);
  }
  .card-front { top: 127px; background: var(--card-dark); }
  .card-back { top: 511px; background: var(--card-light); }

  .wordmark {
    position: absolute;
    left: 0; right: 0;
    text-align: center;
    font-family: "Montserrat", sans-serif;
    font-weight: 800;
    letter-spacing: -2px;
    line-height: 1;
  }
  .card-front .wordmark { top: 88px; font-size: 150px; color: var(--paper); }
  .card-back .wordmark { top: 28px; font-size: 92px; color: var(--ink); }

  .tagline {
    position: absolute;
    top: 287px; left: 0; right: 0;
    text-align: center;
    font-size: 15px;
    letter-spacing: 1.6px;
    color: var(--paper);
  }
  .company-name {
    position: absolute;
    top: 127px; left: 0; right: 0;
    text-align: center;
    font-family: "Montserrat", sans-serif;
    font-weight: 700;
    font-size: 12.5px;
    letter-spacing: 1.2px;
    color: var(--ink);
  }
  .person {
    position: absolute;
    top: 204px;
    right: 305px;
    text-align: right;
  }
  .person-name {
    font-family: "Montserrat", sans-serif;
    font-weight: 700;
    font-size: 17px;
    color: var(--ink);
  }
  .person-title { font-size: 15px; margin-top: 1px; color: var(--ink-soft); }
  .divider {
    position: absolute;
    left: 289px; top: 186px;
    width: 2px; height: 78px;
    background: var(--ink);
  }
  .contacts {
    position: absolute;
    left: 303px; top: 186px;
    list-style: none;
    font-size: 15px;
    color: var(--ink);
  }
  .contacts li { display: flex; align-items: center; height: 19.6px; }
  .contacts svg { width: 13px; height: 13px; margin-right: 5px; flex: none; }
  .areas {
    position: absolute;
    top: 283px; left: 0; right: 0;
    text-align: center;
    font-size: 16px;
    color: var(--ink);
  }
  .emergency {
    position: absolute;
    top: 307px; left: 0; right: 0;
    display: flex;
    justify-content: center;
    align-items: center;
    font-size: 13px;
    color: var(--ink-soft);
  }
  .emergency svg { width: 12px; height: 12px; margin-right: 5px; flex: none; }
</style>
</head>
<body>
  <section class="card card-front">
    <div class="wordmark">HVL</div>
    <p class="tagline">PROPERTIES - PROJECTS - PARTNERS</p>
  </section>

  <section class="card card-back">
    <div class="wordmark">HVL</div>
    <p class="company-name">HARBOR VALE LIVING</p>

    <div class="person">
      <p class="person-name">DANA PRITCHELL</p>
      <p class="person-title">President</p>
    </div>
    <span class="divider"></span>

    <ul class="contacts">
      <li>
        <svg viewBox="0 0 14 14" aria-hidden="true"><rect x="3.5" y="0.8" width="7" height="12.4" rx="1.2" fill="none" stroke="currentColor" stroke-width="1.4"/><circle cx="7" cy="11" r="0.8" fill="currentColor"/></svg>
        (617) 555 0143
      </li>
      <li>
        <svg viewBox="0 0 14 14" aria-hidden="true"><path d="M3 1 L5.5 1 L6.3 4.2 L4.6 5.6 C5.5 7.6 6.6 8.8 8.5 9.6 L9.9 7.8 L13 8.6 L13 11 C13 12.2 12 13 10.8 12.9 C5.6 12.4 1.6 8.4 1.1 3.2 C1 2 1.9 1 3 1 Z" fill="currentColor"/></svg>
        (617) 555 0187
      </li>
      <li>
        <svg viewBox="0 0 14 14" aria-hidden="true"><rect x="0.8" y="2.5" width="12.4" height="9" fill="none" stroke="currentColor" stroke-width="1.3"/><path d="M0.8 2.5 L7 7.5 L13.2 2.5 M0.8 11.5 L5.3 6.3 M13.2 11.5 L8.7 6.3" fill="none" stroke="currentColor" stroke-width="1.1"/></svg>
        dana@harborvaleliving.example
      </li>
      <li>
        <svg viewBox="0 0 14 14" aria-hidden="true"><g fill="none" stroke="currentColor" stroke-width="1.1"><circle cx="7" cy="7" r="6"/><ellipse cx="7" cy="7" rx="2.6" ry="6"/><path d="M1 7 H13 M2 4 H12 M2 10 H12"/></g></svg>
        www.harborvaleliving.example
      </li>
    </ul>

    <p class="areas">Boston | Metrowest | South Shore | Cape | Newport</p>
    <p class="emergency">
      <svg viewBox="0 0 14 14" aria-hidden="true"><path d="M7 0.8 L13.4 12.6 H0.6 Z" fill="currentColor"/><path d="M7 4.8 V8.6" stroke="var(--card-light)" stroke-width="1.5"/><circle cx="7" cy="10.6" r="0.85" fill="var(--card-light)"/></svg>
      After Hours Emergency Support # 1800 555 0199
    </p>
  </section>
</body>
</html>
```